Stonecrest Capital Partners
Business Cards
Project: Stonecrest Capital Partners
Stonecrest Capital Partners - Financial Services
Creative Brief
Simple
Marcus Delane
Managing Director
4625 Ridgeview Parkway Suite 200 Atlanta, GA 30341
Use 678-902-5148 Will supply updated number
mdelane@stonecrestcapital-example.com
www.stonecrestcapital-example.com
The will be business cards for Marcus Delane (Managing Director) and Victor Hollis (Managing Director). Address and phone numbers may change slightly this week. We are not sure if putting cell phones on yet. I once had a very simple business card in a basic font on high quality paper that looked great. Want very simple and professional. The logo can be on the front or keep the front simple and put the logo on the back.
Stonecrest LOGO attached (unless your design has it on the front)

```html
<!DOCTYPE html>
<html lang="en">
<head>
<meta charset="utf-8">
<title>Stonecrest Capital Partners – Business Cards</title>
<link href="https://fonts.googleapis.com/css2?family=Open+Sans:wght@400;600;700&display=swap" rel="stylesheet">
<style>
  :root {
    --page-bg: #e9ecef;
    --card-white: #ffffff;
    --brand-blue: #1f7fc4;
    --brand-deep: #0f5f9c;
    --brand-sky: #4fb0e6;
    --accent-green: #6cbf3f;
    --text-grey: #6b7379;
    --text-dark: #3d4348;
  }
  * { margin: 0; padding: 0; box-sizing: border-box; }
  html, body {
    width: 1200px; height: 901px; overflow: hidden;
    background: var(--page-bg);
    font-family: "Open Sans", Arial, sans-serif;
  }
  .sheet {
    position: relative; width: 1200px; height: 901px;
  }
  .card {
    position: absolute; top: 302px;
    width: 520px; height: 297px;
    border-radius: 18px;
    box-shadow: 0 10px 28px rgba(0,0,0,0.18);
    overflow: hidden;
  }
  .card-front { left: 60px; background: var(--card-white); }
  .card-back {
    left: 620px;
    background: linear-gradient(150deg, var(--brand-sky) 0%, var(--brand-blue) 55%, var(--brand-deep) 100%);
  }
  .brand {
    position: absolute; display: flex; align-items: center; gap: 12px;
  }
  .brand-dot {
    width: 34px; height: 34px; border-radius: 50%;
    background: var(--brand-blue);
  }
  .brand-name {
    font-weight: 600; font-size: 21px; color: var(--brand-blue);
    letter-spacing: 0.2px;
  }
  .card-front .brand { top: 34px; left: 34px; }
  .contact {
    position: absolute; top: 120px; left: 82px;
    color: var(--text-grey); font-size: 10.5px; line-height: 1.5;
  }
  .person-name {
    font-size: 18px; font-weight: 600; color: var(--brand-blue); line-height: 1.2;
  }
  .person-title { font-size: 10.5px; margin-bottom: 12px; }
  .address { margin-bottom: 12px; }
  .line { display: flex; align-items: center; gap: 7px; }
  .line svg { width: 10px; height: 10px; flex: none; }
  .card-back .brand { right: 34px; bottom: 40px; }
  .card-back .brand-name { color: var(--card-white); font-size: 23px; }
</style>
</head>
<body>
<main class="sheet">
  <section class="card card-front" aria-label="Card front">
    <div class="brand">
      <span class="brand-dot"></span>
      <span class="brand-name">Stonecrest Capital Partners</span>
    </div>
    <div class="contact">
      <p class="person-name">Marcus Delane</p>
      <p class="person-title">Managing Director</p>
      <p class="address">4625 Ridgeview Parkway Suite 200<br>Atlanta, GA 30341</p>
      <p class="line">
        <svg viewBox="0 0 10 10"><path d="M2 1 L4 1 L4.6 3 L3.4 3.8 Q4.4 5.8 6.2 6.6 L7 5.4 L9 6 L9 8 Q8.6 9 7.6 9 Q1 8 1 2.4 Q1 1 2 1Z" fill="var(--accent-green)"/></svg>
        678-902-5148
      </p>
      <p class="line">
        <svg viewBox="0 0 10 10"><rect x="0.5" y="2" width="9" height="6" rx="1" fill="var(--accent-green)"/><path d="M0.8 2.4 L5 5.6 L9.2 2.4" stroke="#fff" stroke-width="0.8" fill="none"/></svg>
        mdelane@stonecrestcapital-example.com
      </p>
      <p class="line">
        <svg viewBox="0 0 10 10"><circle cx="5" cy="5" r="4.2" fill="none" stroke="var(--accent-green)" stroke-width="1"/><ellipse cx="5" cy="5" rx="1.8" ry="4.2" fill="none" stroke="var(--accent-green)" stroke-width="0.8"/><line x1="0.8" y1="5" x2="9.2" y2="5" stroke="var(--accent-green)" stroke-width="0.8"/></svg>
        www.stonecrestcapital-example.com
      </p>
    </div>
  </section>

  <section class="card card-back" aria-label="Card back">
    <div class="brand">
      <span class="brand-name">Stonecrest Capital Partners</span>
    </div>
  </section>
</main>
</body>
</html>
```